Web App Dashboard Design for a Smart Home

We are a company that gives consultancy and installation services for custom smart home designs to household owners in ON, Canada. For our web application, we are in need of a dashboard design which will display multiple rooms that could be present in a home. This should be a flexible design as the number of rooms where smart devices installed will vary from house to house. We would like to see the name of the rooms and several icons that represent different monitored objects in each room like temperature, light on/off, sound/music on/off, humidity, illuminance, noise level, air quality, for bathrooms and kitchens wet/dry conditions, windows/doors open, curtains open/closed etc. The web application will collect the latest status data from all related sensors and it will be publishing the latest status for each room into this dashboard. Backend of the dashboards should contain nice modern looking houses and it would be good if there are multiple versions of the background pictures that rotate.

Target Market(s)

Mid-Market range house holders who want to increase their comfort and safety with smart home implementations

Industry/Entity Type

Small Business

Number of Pages Required

1 page

Colors
0455a3
3277b5
85acd3
86cae7
fbf289
cadf82
acd037
9bcb3c
faa54b

Requirements
Must have
• - A Flexible Dashboard Design which can hold many rooms but still look sharp even with only 1/2 rooms as well.
• - An smart home icon library that will show the monitored value like temperature, lights on/off, door/window open/close etc.

```html
<!DOCTYPE html>
<html lang="en">
<head>
<meta charset="utf-8">
<title>Smart Home Dashboard</title>
<link href="https://fonts.googleapis.com/css2?family=Nunito+Sans:wght@400;600;700&display=swap" rel="stylesheet">
<style>
:root{
  --brand-blue:#0455a3;
  --orange:#faa54b;
  --green:#9bcb3c;
  --lime:#acd037;
  --yellow:#fbf289;
  --sky:#86cae7;
  --red:#d64541;
  --panel:rgba(38,44,52,.82);
  --panel-soft:rgba(40,46,54,.5);
  --text:#ffffff;
  --muted:#d6dbe1;
}
*{box-sizing:border-box;margin:0;padding:0}
html,body{width:1200px;height:675px;overflow:hidden}
body{font-family:"Nunito Sans",sans-serif;color:var(--text);position:relative;background:#1f262e}
.backdrop{position:absolute;inset:74px 0 0 0;background:
  radial-gradient(ellipse at 50% 35%,#4a4d52 0%,#33383f 45%,#262c33 100%);}
.backdrop::after{content:"";position:absolute;left:0;right:0;bottom:0;height:220px;
  background:linear-gradient(180deg,rgba(60,66,60,0) 0%,rgba(58,64,54,.7) 60%,rgba(52,58,48,.9) 100%)}
.topbar{position:absolute;left:0;top:0;width:1200px;height:74px;background:var(--brand-blue);
  display:flex;align-items:center;padding:0 30px}
.brand{font-size:26px;font-weight:600;letter-spacing:.3px}
.user{margin-left:auto;display:flex;align-items:center;gap:14px;font-size:16px}
.bell{position:relative;width:22px;height:22px;margin-right:6px}
.bell .badge{position:absolute;right:-6px;bottom:-4px;width:12px;height:12px;border-radius:50%;
  background:var(--red);font-size:7px;text-align:center;line-height:12px}
.main{position:absolute;inset:74px 0 0 0}
.home-title{position:absolute;left:31px;top:36px;font-size:26px;font-weight:600;display:flex;align-items:center;gap:16px}
.edit-btn{width:22px;height:22px;border-radius:3px;background:var(--red);display:flex;align-items:center;justify-content:center}
.tabs{position:absolute;left:420px;top:39px;display:flex;align-items:center;gap:13px}
.tab{height:24px;padding:0 10px;border:1px solid #e6e6e6;border-radius:2px;font-size:12px;line-height:22px}
.tab.active{background:var(--orange);border-color:var(--orange)}
.tab.kitchen{width:72px;text-align:center}
.tab.bedrooms{width:72px;text-align:center}
.updated{position:absolute;right:31px;top:39px;display:flex;align-items:center;gap:10px;font-size:12px}
.refresh{width:22px;height:22px;border-radius:2px;background:var(--lime);display:flex;align-items:center;justify-content:center}
.filter{position:absolute;left:31px;top:88px;height:16px;display:flex;align-items:center;gap:6px;color:var(--orange);font-size:12px}
.group{position:absolute;left:31px;width:1138px;height:43px;background:var(--panel);border-radius:2px;
  display:flex;align-items:center;padding:0 12px;font-size:12px;gap:10px}
.group.open{top:122px}
.group.bath{top:414px;background:var(--panel-soft)}
.group.living{top:470px}
.group.kitchen-row{top:526px}
.group.extra{top:582px}
.group .chev{margin-left:auto}
.cards{position:absolute;left:31px;top:184px;display:flex;gap:21px}
.card{width:210px;height:210px;background:rgba(42,47,54,.92);border-radius:2px;overflow:hidden;position:relative}
.photo{height:140px}
.photo.master{background:linear-gradient(160deg,#4a2d2a 0%,#6b4a3d 50%,#d9d4cf 100%)}
.photo.kids1{background:linear-gradient(160deg,#5b7aa3 0%,#b9c0c8 55%,#3d4a5c 100%)}
.photo.kids2{background:linear-gradient(170deg,#2d2a24 0%,#b8a98d 45%,#e6ddcf 100%)}
.photo.guest{background:linear-gradient(170deg,#e3dbcd 0%,#cbbfae 55%,#a08a6c 100%)}
.room-name{font-size:13px;padding:7px 10px 0}
.stats{display:flex;align-items:center;gap:10px;padding:4px 12px 0;font-size:13px}
.stat{display:flex;align-items:center;gap:5px}
.expand{position:absolute;left:50%;bottom:8px;transform:translateX(-50%)}
.card.add{background:rgba(42,47,54,.7);display:flex;flex-direction:column;align-items:center;justify-content:center;gap:10px;font-size:12px;font-weight:600}
.add-btn{width:50px;height:50px;border-radius:50%;background:var(--red);display:flex;align-items:center;justify-content:center;margin-top:-28px}
</style>
</head>
<body>
<div class="backdrop" role="img" aria-label="Modern two-storey suburban house at dusk with front lawn and landscaping"></div>

<header class="topbar">
  <div class="brand">Company Logo</div>
  <div class="user">
    <div class="bell">
      <svg width="18" height="20" viewBox="0 0 18 20"><path d="M9 1c3.5 0 5.5 2.6 5.5 6v4l2 3H1.5l2-3V7C3.5 3.6 5.5 1 9 1z" fill="#fff"/><circle cx="9" cy="17" r="2" fill="#fff"/></svg>
      <span class="badge">1</span>
    </div>
    <svg width="32" height="32" viewBox="0 0 32 32"><circle cx="16" cy="16" r="14.5" fill="none" stroke="#fff" stroke-width="3"/><circle cx="16" cy="12" r="5" fill="#fff"/><path d="M7 25c2-5 16-5 18 0" fill="#fff"/></svg>
    <span>Alex Morgan</span>
  </div>
</header>

<main class="main">
  <div class="home-title">Alex's Home
    <span class="edit-btn"><svg width="10" height="10" viewBox="0 0 10 10"><path d="M1 9l1-3 5-5 2 2-5 5z" fill="#fff"/></svg></span>
  </div>

  <nav class="tabs">
    <svg width="8" height="12" viewBox="0 0 8 12"><path d="M8 0v12L0 6z" fill="#c9ccd0"/></svg>
    <span class="tab active">All Rooms</span>
    <span class="tab kitchen">Kitchen</span>
    <span class="tab bedrooms">Bedrooms</span>
    <span class="tab">Bathrooms</span>
    <svg width="8" height="12" viewBox="0 0 8 12"><path d="M0 0v12l8-6z" fill="#9bcb3c"/></svg>
  </nav>

  <div class="updated">Last updated: 30 mins ago
    <span class="refresh"><svg width="12" height="12" viewBox="0 0 12 12"><path d="M10 4A4.5 4.5 0 0 0 2 5M2 8a4.5 4.5 0 0 0 8-1" stroke="#fff" stroke-width="1.6" fill="none"/><path d="M10 1v3.5H6.5zM2 11V7.5h3.5z" fill="#fff"/></svg></span>
  </div>

  <div class="filter">
    <svg width="12" height="12" viewBox="0 0 12 12"><path d="M0 0h12L7 6v6L5 10V6z" fill="#faa54b"/></svg>All Rooms
  </div>

  <div class="group open">
    <svg width="20" height="14" viewBox="0 0 20 14"><path d="M1 1v12M19 7v6M1 10h18M1 7h18" stroke="#fff" stroke-width="2"/><rect x="3" y="3" width="4" height="4" fill="#fff"/><rect x="8" y="4" width="11" height="3" fill="#fff"/></svg>
    Bedrooms
    <svg class="chev" width="14" height="8" viewBox="0 0 14 8"><path d="M0 0h14L7 8z" fill="#fff"/></svg>
  </div>

  <section class="cards">
    <article class="card">
      <div class="photo master" role="img" aria-label="Master bedroom with large bed and dark wood walls"></div>
      <div class="room-name">Master Bedroom</div>
      <div class="stats">
        <span class="stat"><svg width="8" height="14" viewBox="0 0 8 14"><rect x="2.5" y="0.5" width="3" height="9" rx="1.5" fill="none" stroke="#cadf82"/><circle cx="4" cy="11" r="2.5" fill="#cadf82"/></svg>35°C</span>
        <span class="stat"><svg width="9" height="12" viewBox="0 0 9 12"><path d="M4.5 0C6 3 9 5.5 9 8a4.5 4.5 0 0 1-9 0c0-2.5 3-5 4.5-8z" fill="#3277b5"/></svg>35%</span>
        <span class="stat"><svg width="8" height="12" viewBox="0 0 8 12"><circle cx="4" cy="4" r="4" fill="#fbf289"/><rect x="2.5" y="8" width="3" height="3" fill="#fbf289"/></svg>3</span>
        <span class="stat"><svg width="11" height="10" viewBox="0 0 11 10"><path d="M0 3h3l4-3v10L3 7H0z" fill="#86cae7"/></svg>40dB</span>
      </div>
      <svg class="expand" width="14" height="8" viewBox="0 0 14 8"><path d="M0 0h14L7 8z" fill="#fff"/></svg>
    </article>
    <article class="card">
      <div class="photo kids1" role="img" aria-label="Kids bedroom with blue walls, desk and single bed"></div>
      <div class="room-name">Kids Bedroom 1</div>
      <div class="stats">
        <span class="stat"><svg width="8" height="14" viewBox="0 0 8 14"><rect x="2.5" y="0.5" width="3" height="9" rx="1.5" fill="none" stroke="#cadf82"/><circle cx="4" cy="11" r="2.5" fill="#cadf82"/></svg>35°C</span>
        <span class="stat"><svg width="9" height="12" viewBox="0 0 9 12"><path d="M4.5 0C6 3 9 5.5 9 8a4.5 4.5 0 0 1-9 0c0-2.5 3-5 4.5-8z" fill="#3277b5"/></svg>35%</span>
        <span class="stat"><svg width="8" height="12" viewBox="0 0 8 12"><circle cx="4" cy="4" r="4" fill="#fbf289"/><rect x="2.5" y="8" width="3" height="3" fill="#fbf289"/></svg>3</span>
        <span class="stat"><svg width="11" height="10" viewBox="0 0 11 10"><path d="M0 3h3l4-3v10L3 7H0z" fill="#86cae7"/></svg>40dB</span>
      </div>
      <svg class="expand" width="14" height="8" viewBox="0 0 14 8"><path d="M0 0h14L7 8z" fill="#fff"/></svg>
    </article>
    <article class="card">
      <div class="photo kids2" role="img" aria-label="Cosy kids bedroom with soft toy on the bed and string lights"></div>
      <div class="room-name">Kids Bedroom 2</div>
      <div class="stats">
        <span class="stat"><svg width="8" height="14" viewBox="0 0 8 14"><rect x="2.5" y="0.5" width="3" height="9" rx="1.5" fill="none" stroke="#cadf82"/><circle cx="4" cy="11" r="2.5" fill="#cadf82"/></svg>35°C</span>
        <span class="stat"><svg width="9" height="12" viewBox="0 0 9 12"><path d="M4.5 0C6 3 9 5.5 9 8a4.5 4.5 0 0 1-9 0c0-2.5 3-5 4.5-8z" fill="#3277b5"/></svg>35%</span>
        <span class="stat"><svg width="8" height="12" viewBox="0 0 8 12"><circle cx="4" cy="4" r="4" fill="#fbf289"/><rect x="2.5" y="8" width="3" height="3" fill="#fbf289"/></svg>3</span>
        <span class="stat"><svg width="11" height="10" viewBox="0 0 11 10"><path d="M0 3h3l4-3v10L3 7H0z" fill="#86cae7"/></svg>40dB</span>
      </div>
      <svg class="expand" width="14" height="8" viewBox="0 0 14 8"><path d="M0 0h14L7 8z" fill="#fff"/></svg>
    </article>
    <article class="card">
      <div class="photo guest" role="img" aria-label="Bright guest bedroom with desk and neatly made bed"></div>
      <div class="room-name">Guest Bedroom</div>
      <div class="stats">
        <span class="stat"><svg width="8" height="14" viewBox="0 0 8 14"><rect x="2.5" y="0.5" width="3" height="9" rx="1.5" fill="none" stroke="#cadf82"/><circle cx="4" cy="11" r="2.5" fill="#cadf82"/></svg>35°C</span>
        <span class="stat"><svg width="9" height="12" viewBox="0 0 9 12"><path d="M4.5 0C6 3 9 5.5 9 8a4.5 4.5 0 0 1-9 0c0-2.5 3-5 4.5-8z" fill="#3277b5"/></svg>35%</span>
        <span class="stat"><svg width="8" height="12" viewBox="0 0 8 12"><circle cx="4" cy="4" r="4" fill="#fbf289"/><rect x="2.5" y="8" width="3" height="3" fill="#fbf289"/></svg>3</span>
        <span class="stat"><svg width="11" height="10" viewBox="0 0 11 10"><path d="M0 3h3l4-3v10L3 7H0z" fill="#86cae7"/></svg>40dB</span>
      </div>
      <svg class="expand" width="14" height="8" viewBox="0 0 14 8"><path d="M0 0h14L7 8z" fill="#fff"/></svg>
    </article>
    <article class="card add">
      <span class="add-btn"><svg width="16" height="16" viewBox="0 0 16 16"><path d="M8 1v14M1 8h14" stroke="#fff" stroke-width="2"/></svg></span>
      Add Bedroom
    </article>
  </section>

  <div class="group bath">
    <svg width="20" height="14" viewBox="0 0 20 14"><path d="M1 1v12M19 7v6M1 10h18M1 7h18" stroke="#fff" stroke-width="2"/><rect x="3" y="3" width="4" height="4" fill="#fff"/><rect x="8" y="4" width="11" height="3" fill="#fff"/></svg>
    Bathrooms
    <svg class="chev" width="8" height="12" viewBox="0 0 8 12"><path d="M0 0v12l8-6z" fill="#fff"/></svg>
  </div>
  <div class="group living">
    <svg width="20" height="14" viewBox="0 0 20 14"><rect x="4" y="1" width="12" height="6" rx="2" fill="#fff"/><path d="M1 5h3v5h12V5h3v7H1z" fill="#fff"/></svg>
    Living Rooms
    <svg class="chev" width="8" height="12" viewBox="0 0 8 12"><path d="M0 0v12l8-6z" fill="#fff"/></svg>
  </div>
  <div class="group kitchen-row">
    <svg width="20" height="16" viewBox="0 0 20 16"><rect x="3" y="5" width="14" height="10" rx="1" fill="#fff"/><rect x="1" y="4" width="18" height="2" fill="#fff"/><rect x="8" y="1" width="4" height="2" fill="#fff"/></svg>
    Kitchen
    <svg class="chev" width="8" height="12" viewBox="0 0 8 12"><path d="M0 0v12l8-6z" fill="#fff"/></svg>
  </div>
  <div class="group extra">
    <svg width="20" height="14" viewBox="0 0 20 14"><path d="M1 1v12M19 7v6M1 10h18M1 7h18" stroke="#fff" stroke-width="2"/><rect x="3" y="3" width="4" height="4" fill="#fff"/><rect x="8" y="4" width="11" height="3" fill="#fff"/></svg>
    Utility Room
    <svg class="chev" width="8" height="12" viewBox="0 0 8 12"><path d="M0 0v12l8-6z" fill="#fff"/></svg>
  </div>
</main>
</body>
</html>
```